Stationary design for Velora Skin
the art and science of skin care
Dennis O. Pawlak, M.D.
1.2716 Fenwick Ave.
Millbrook, Utah 84512
2. 218 West 700 North Suite 4
Larkfield, Utah 84127
1-800-wellpath
dennispaw@mailbrook.net
www.veloraskin.com
The business card will be plastic cards.Pinted on one side. Please wow us with the design. Use the logo of my last project #383, 382, 381 in the design
I need envelopes, stationary and plastic busniess card designs

```html
<!DOCTYPE html>
<html lang="en">
<head>
<meta charset="utf-8">
<title>Velora Skin – Business Card</title>
<link rel="stylesheet" href="https://fonts.googleapis.com/css2?family=Cinzel:wght@500&family=Questrial&display=swap">
<style>
  :root {
    --page-bg: #ece8e4;
    --card-bg: #f6f4f5;
    --card-edge: #dcd7d9;
    --brand-pink: #e6177e;
    --ink: #2b2326;
    --ink-soft: #4a4145;
  }
  * { margin: 0; padding: 0; box-sizing: border-box; }
  html, body {
    width: 1200px;
    height: 901px;
    overflow: hidden;
    background: var(--page-bg);
  }
  .business-card {
    position: absolute;
    left: 100px;
    top: 160px;
    width: 1000px;
    height: 580px;
    border-radius: 24px;
    background: var(--card-bg);
    border: 1px solid var(--card-edge);
    box-shadow: 0 18px 40px rgba(60, 40, 50, 0.18);
    overflow: hidden;
  }
  .artwork-panel {
    position: absolute;
    right: 0;
    top: 0;
    width: 440px;
    height: 580px;
  }
  .brand-block {
    position: absolute;
    left: 64px;
    top: 60px;
    width: 480px;
  }
  .brand-name {
    font-family: "Cinzel", serif;
    font-weight: 500;
    font-size: 64px;
    letter-spacing: 3px;
    color: var(--ink);
    line-height: 1;
  }
  .brand-tagline {
    margin-top: 8px;
    font-family: "Questrial", sans-serif;
    font-size: 13px;
    letter-spacing: 1.5px;
    color: var(--brand-pink);
    text-transform: lowercase;
  }
  .doctor-name {
    position: absolute;
    left: 64px;
    top: 205px;
    font-family: "Questrial", sans-serif;
    font-size: 30px;
    letter-spacing: 3px;
    color: var(--ink);
    text-transform: uppercase;
  }
  .contact-details {
    position: absolute;
    left: 64px;
    top: 275px;
    font-family: "Questrial", sans-serif;
    font-size: 15px;
    line-height: 22px;
    color: var(--ink-soft);
  }
  .contact-lines {
    display: grid;
    grid-template-columns: 78px auto;
    margin-top: 10px;
  }
  .contact-label { color: var(--ink); }
  .website {
    position: absolute;
    left: 0;
    width: 560px;
    bottom: 46px;
    text-align: center;
    font-family: "Questrial", sans-serif;
    font-size: 20px;
    letter-spacing: 0.5px;
    color: var(--brand-pink);
  }
</style>
</head>
<body>
  <div class="business-card">
    <svg class="artwork-panel" viewBox="0 0 440 580" role="img"
         aria-label="Illustration of a woman's profile silhouette with white orchids in her flowing hair">
      <defs>
        <linearGradient id="panelPink" x1="0" y1="0" x2="1" y2="1">
          <stop offset="0" stop-color="#ef3d95"/>
          <stop offset="1" stop-color="#d8106e"/>
        </linearGradient>
        <radialGradient id="bloomGlow" cx="0.55" cy="0.2" r="0.45">
          <stop offset="0" stop-color="#fbe3ef"/>
          <stop offset="1" stop-color="#fbe3ef" stop-opacity="0"/>
        </radialGradient>
      </defs>
      <path d="M120 0 H440 V580 H40 C90 460 70 330 110 220 C140 140 100 70 120 0 Z" fill="url(#panelPink)"/>
      <rect x="100" y="0" width="340" height="300" fill="url(#bloomGlow)"/>
    </svg>

    <div class="brand-block">
      <div class="brand-name">VELORA</div>
      <div class="brand-tagline">the art &amp; science of skin care</div>
    </div>

    <div class="doctor-name">Dennis O. Pawlak, M.D</div>

    <div class="contact-details">
      <p>1. 2716 Fenwick Ave.</p>
      <p>Millbrook, Utah 84512</p>
      <p>2. 218 West 700 North Suite 4</p>
      <p>Larkfield, Utah 84127</p>
      <div class="contact-lines">
        <span class="contact-label">Toll free:</span><span>1-800-wellpath</span>
        <span class="contact-label">Phone:</span><span>1-801-555-0142</span>
        <span class="contact-label">Fax:</span><span>1-801-555-0178</span>
        <span class="contact-label">Email:</span><span>dennispaw@mailbrook.net</span>
      </div>
    </div>

    <div class="website">www.veloraskin.com</div>
  </div>
</body>
</html>
```